Design an engaging, visually attractive and well laid out Word Press website

I have a partially completed Word Press website that I need to have completed . The previous designer overestimated her ability to produce a quality product and underestimated my knowledge of how a good well designed website should look visually and be laid out.

A visitor to the site should have a clear understanding of the services offered by the business, be able to navigate the site with ease via effective logical pathways, have calls to action that are prominent and located in the correct locations that prompt the viewer to make contact when they are ready to act. The site needs to be visually impactful, have lots of white space, fast loading and mobile compatible and the visitor needs to have the impression that they need to look no further for the services offered.

I am particularly interested in how you think the Services and Projects pages should be best laid out so they present well on a mobile device without looking cluttered and can be navigated and viewed with ease.

I have the copy and images (these may need some changes) and I have put together a basic version of a layout on MS Word documents. These are all in a Dropbox folder (link below). I am open to a designer offering his/her own thoughts on how the site can be laid out better. Also I have a link below to the partially created website. I will need the website coded once I am happy with the design.

Links:

https://larkvale.com.au?bypass=moor

https://www.filecrate.net/sh/qwprtz8m3x204kd/BBXQwerTyuIopAsDfGhJkL-9z?dl=0

Target Market(s)

Primarily females aged 19 - 65 who work for a strata management and/or a property management company. These organisations oversee the maintenance aspects for apartments/condominiums and manage the properties on behalf of the owners.
The business that the website represents provides professional gardening services for commercial businesses and these apartment/condominium communities. So do not think home gardens and that type of gardening. Think on a larger scale like commercial businesses, hospitals, blocks of units/apartments/condominiums, shopping centres.

Industry/Entity Type

Commercial

Coding

Coded - Design and coding required

Number of Pages Required

5+ page

Requirements
Must have
• A great layout with lots of white space, intuitive navigation, prominent calls to action and professional looking.

The website needs to give the impression that the business is mid-size with a number of employees i.e. 6-10, yet still have the impression that it is a business where the owner is involved and there is a high level of personalised customer service.
Nice to have
• Maybe a looping video on the home page that is faded in the background that represents what the business does and who it services.
Should not have
• An attitude by the designer that anything will satisfy me. I want the designer to create a design that they would be proud to present to the market.

I have had too many bad experiences with website designers who do not have the appropriate attitude or skills to produce a quality site that appeals to me.

```html
<!DOCTYPE html>
<html lang="en">
<head>
<meta charset="utf-8">
<title>Larkvale — Scheduled Garden Care Programs</title>
<link rel="stylesheet" href="https://fonts.googleapis.com/css2?family=Fira+Sans:wght@400;500;600&family=Open+Sans:wght@400;600;700&display=swap">
<style>
:root{
  --green:#6aab2c;
  --green-dark:#4f8a1c;
  --ink:#2b2b2b;
  --text:#444;
  --muted:#777;
  --line:#d8d8d8;
  --grey-band:#e9e9e9;
  --dark:#1e1e1e;
  --white:#fff;
}
*{box-sizing:border-box;margin:0;padding:0}
html,body{width:1200px;height:5367px;overflow:hidden}
body{font-family:"Open Sans",sans-serif;color:var(--text);background:var(--white);position:relative}
.section{position:relative;width:1200px;overflow:hidden}
.wrap{position:absolute;left:144px;width:912px}
h2,.display{font-family:"Fira Sans",sans-serif;font-weight:500}
.btn{display:inline-block;background:var(--green);color:var(--white);border-radius:40px;font-family:"Open Sans",sans-serif;font-weight:700;text-transform:uppercase;text-align:center}

/* hero */
.hero{height:720px;background:linear-gradient(180deg,#3b3a2a 0%,#5a5b36 40%,#5f7a2a 75%,#6c8e30 100%)}
.hero .photo{position:absolute;inset:0}
.navbar{position:absolute;left:144px;top:17px;width:912px;height:79px;background:var(--white);border-radius:4px;display:flex;align-items:center;padding:0 24px}
.brand{display:flex;align-items:center;gap:12px}
.brand-mark{width:30px;height:30px;border-radius:50%;background:var(--green)}
.brand-name{font-family:"Fira Sans",sans-serif;font-size:26px;font-weight:500;color:var(--ink)}
.nav-right{margin-left:auto;display:flex;align-items:center;gap:26px}
.nav-phone{display:flex;align-items:center;gap:8px;font-family:"Fira Sans",sans-serif;font-size:26px;color:#555}
.nav-quote{padding:10px 18px;font-size:14px}
.burger{width:26px;display:flex;flex-direction:column;gap:5px}
.burger span{height:3px;background:#888;display:block}
.hero-copy{position:absolute;left:0;width:1200px;top:255px;text-align:center;color:var(--white)}
.play{width:62px;height:62px;margin:0 auto 20px}
.hero-title{font-family:"Fira Sans",sans-serif;font-size:38px;font-weight:500;line-height:46px;text-transform:uppercase}
.hero-sub{font-size:18px;margin-top:10px}
.hero-cut{position:absolute;left:0;bottom:0;width:1200px;height:110px}

/* intro */
.intro{height:509px;background:linear-gradient(90deg,#fff 0%,#f4f4f4 55%,#e5e5e5 100%)}
.intro .portrait{position:absolute;left:0;top:50px;width:480px;height:459px;background:radial-gradient(circle at 45% 35%,#c98a5a 0%,#8a5a32 35%,#e97a1c 70%,#222 100%)}
.intro .watermark{position:absolute;left:330px;top:70px;width:300px;height:300px;border-radius:50%;background:rgba(120,120,120,.15)}
.intro-lead{position:absolute;left:631px;top:70px;width:440px;font-family:"Fira Sans",sans-serif;font-size:33px;line-height:45px;color:var(--green)}
.intro-body{position:absolute;left:639px;top:300px;width:420px;font-size:16px;line-height:32px;color:#333}

/* services */
.services{height:615px}
.services h2{position:absolute;left:144px;top:75px;font-size:40px;color:var(--green)}
.services .lead{position:absolute;left:144px;top:150px;width:410px;font-size:19px;line-height:34px;color:#333}
.services .btn{position:absolute;left:144px;top:405px;padding:10px 24px;font-size:14px}
.cards{position:absolute;left:604px;top:79px;width:452px;display:grid;grid-template-columns:217px 217px;gap:15px 18px}
.card{height:221px;border:2px solid #a9d47e;background:var(--white);text-align:center;padding:6px}
.card .thumb{height:72px;background:linear-gradient(180deg,#5b6b4a,#3f5a2a 60%,#6b8a3a)}
.card h3{font-family:"Open Sans",sans-serif;font-size:14px;font-weight:700;color:#222;margin:14px 4px 8px;text-transform:uppercase;line-height:18px}
.card p{font-size:10px;line-height:16px;color:var(--muted);padding:0 12px}
.card .go{width:18px;height:18px;margin:12px auto 0}

/* cta bands */
.cta{height:479px;background:linear-gradient(180deg,#2a2622,#3d362f 55%,#2a2622);text-align:center;color:var(--white)}
.cta .inner{position:absolute;left:0;width:1200px}
.cta-one .inner{top:155px}
.cta-one h2{font-size:32px;font-weight:500}
.cta-one p{font-size:16px;margin-top:14px}
.cta-one .btn{margin-top:14px;padding:16px 38px;font-size:30px;font-family:"Fira Sans",sans-serif;font-weight:500}

/* recent work */
.work{height:729px;text-align:center}
.work h2{position:absolute;left:0;width:1200px;top:75px;font-size:40px;color:var(--green)}
.work .lead{position:absolute;left:0;width:1200px;top:140px;font-size:19px;color:#333}
.gallery{position:absolute;left:144px;top:189px;width:912px;display:grid;grid-template-columns:repeat(12,1fr);grid-template-rows:192px 192px;gap:6px}
.tile{display:block}
.g1{grid-column:span 3;background:linear-gradient(135deg,#2f5a22,#4d7a2e 50%,#b33a3a)}
.g2{grid-column:span 3;background:linear-gradient(180deg,#9aa78c,#5f6b3f)}
.g3{grid-column:span 6;background:linear-gradient(180deg,#c9a9a6 0%,#b1263a 55%,#7a1b22)}
.g4{grid-column:span 6;background:linear-gradient(135deg,#d8e9b0,#6f9d2a 55%,#3f6a18)}
.g5{grid-column:span 3;background:linear-gradient(180deg,#8fa7b8,#4b6a32 50%,#7a8a3a)}
.g6{grid-column:span 3;background:linear-gradient(180deg,#3a5a2a,#6fa03a 50%,#9cc45a)}
.work .btn{position:absolute;left:543px;top:2950px;padding:10px 24px;font-size:14px;top:627px}

/* clients */
.clients{height:323px;background:var(--grey-band);text-align:center}
.clients h2{position:absolute;left:0;width:1200px;top:70px;font-size:40px;color:var(--green)}
.logos{position:absolute;left:144px;top:150px;width:912px;height:90px;display:flex;align-items:center}
.logo{flex:1;text-align:center;font-family:"Open Sans",sans-serif;font-weight:600;font-size:18px;color:#555;border-right:1px solid #cfcfcf;height:80px;line-height:80px}
.logo:last-child{border-right:none}
.arrow{position:absolute;top:175px;width:22px;height:40px}

/* testimonial */
.quote-sec{height:594px}
.ring{position:absolute;left:143px;top:80px;width:430px;height:430px;border-radius:50%;border:2px solid #cfe6b6;background:var(--white)}
.ring .photo{position:absolute;left:22px;top:22px;width:382px;height:382px;border-radius:50%;background:radial-gradient(circle at 55% 40%,#e9e2c6 0%,#7a7a3a 40%,#3a4a1a 100%)}
.quote-sec h2{position:absolute;left:632px;top:92px;font-size:40px;line-height:46px;color:var(--green)}
.quote-sec blockquote{position:absolute;left:632px;top:222px;width:430px;font-size:22px;line-height:40px;color:#333}
.quote-sec cite{position:absolute;left:632px;top:400px;font-style:normal;font-family:"Fira Sans",sans-serif;font-size:26px;color:#222}
.pager{position:absolute;left:632px;top:467px;display:flex;gap:12px}
.pager span{width:22px;height:22px;border:1px solid #666;display:flex;align-items:center;justify-content:center}

.cta-two{background:linear-gradient(180deg,#3a2a1a,#6a4a22 45%,#2e2418)}
.cta-two .inner{top:140px}
.cta-two h2{font-size:32px;line-height:48px;padding:0 140px;font-weight:500}
.cta-two .btn{margin-top:24px;padding:16px 36px;font-size:30px;font-family:"Fira Sans",sans-serif;font-weight:500}

/* request */
.request{height:552px;text-align:center}
.request h2{position:absolute;left:0;width:1200px;top:75px;font-size:40px;color:var(--green)}
.request .lead{position:absolute;left:144px;width:912px;top:142px;font-size:14px;line-height:28px;color:#444}
.request .lead strong{color:var(--green);font-weight:600}
.form{position:absolute;left:144px;top:232px;width:912px;height:90px}
.field{position:absolute;height:40px;border:1px solid #bbb;font-size:12px;color:#777;text-align:left;padding:10px 14px}
.field.msg{height:88px}
.request .btn{position:absolute;left:544px;top:355px;padding:10px 28px;font-size:14px}

/* footer */
.footer{height:450px;background:var(--dark);color:#bbb}
.footer .peak{position:absolute;left:0;top:0;width:1200px;height:90px}
.f-brand{position:absolute;left:144px;top:163px;display:flex;align-items:center;gap:12px}
.f-brand .brand-mark{background:#555}
.f-brand .brand-name{color:#aaa}
.f-about{position:absolute;left:144px;top:235px;width:330px;font-size:15px;line-height:28px;color:#aaa}
.f-col h4{font-family:"Fira Sans",sans-serif;font-weight:500;font-size:19px;color:#eee;margin-bottom:20px}
.f-contact{position:absolute;left:628px;top:158px}
.f-contact p{font-size:12px;margin-bottom:14px;display:flex;gap:12px;align-items:center}
.socials{display:flex;gap:12px;margin-top:14px}
.socials span{width:42px;height:42px;border-radius:50%;border:1px solid #888;display:flex;align-items:center;justify-content:center;font-size:13px;color:#ccc}
.f-nav{position:absolute;left:962px;top:158px}
.f-nav li{list-style:none;font-size:12px;line-height:27px}
.f-rule{position:absolute;left:144px;top:392px;width:912px;height:1px;background:#3a3a3a}
.f-copy{position:absolute;left:0;width:1200px;top:418px;text-align:center;font-size:12px;color:#999}
</style>
</head>
<body>

<header class="section hero">
  <div class="photo" role="img" aria-label="Gardener in a hard hat tending plants in a garden bed"></div>
  <nav class="navbar">
    <div class="brand"><span class="brand-mark"></span><span class="brand-name">Larkvale</span></div>
    <div class="nav-right">
      <span class="nav-phone">
        <svg width="20" height="20" viewBox="0 0 24 24"><path fill="#666" d="M6.6 10.8a15.1 15.1 0 0 0 6.6 6.6l2.2-2.2c.3-.3.7-.4 1-.2 1.1.4 2.3.6 3.6.6.6 0 1 .4 1 1V20c0 .6-.4 1-1 1A17 17 0 0 1 3 4c0-.6.4-1 1-1h3.5c.6 0 1 .4 1 1 0 1.3.2 2.5.6 3.6.1.3 0 .7-.2 1z"/></svg>
        0400 555 182</span>
      <span class="btn nav-quote">Request a quote</span>
      <span class="burger"><span></span><span></span><span></span></span>
    </div>
  </nav>
  <div class="hero-copy">
    <svg class="play" viewBox="0 0 62 62"><circle cx="31" cy="31" r="29" fill="none" stroke="#fff" stroke-width="2"/><path d="M25 19l17 12-17 12z" fill="none" stroke="#fff" stroke-width="2"/></svg>
    <h1 class="hero-title">Scheduled garden care programs and<br>garden maintenance services</h1>
    <p class="hero-sub">for residential, strata and commercial properties</p>
  </div>
  <svg class="hero-cut" viewBox="0 0 1200 110" preserveAspectRatio="none"><path d="M0 0 L600 110 L1200 0 L1200 110 L0 110 Z" fill="#fff"/></svg>
</header>

<section class="section intro">
  <div class="watermark" aria-hidden="true"></div>
  <div class="portrait" role="img" aria-label="Smiling business owner in a wide-brim hat and high-visibility shirt"></div>
  <p class="intro-lead">At Larkvale we offer quality professional workmanship and strive to exceed expectations and deliver value</p>
  <p class="intro-body">And because of that we are trusted by the WAMC and many Strata Management, Property Management and Aged Care organisations throughout the Perth metropolitan region.</p>
</section>

<section class="section services">
  <h2>Our Services</h2>
  <p class="lead">Larkvale provides a full complement of garden services for residential, strata and commercial properties.<br><br>In addition to our core garden services, we use strategic partners to undertake highly specialised tasks.</p>
  <span class="btn">View all our services</span>
  <div class="cards">
    <article class="card">
      <div class="thumb" role="img" aria-label="Tidy garden bed beside a path"></div>
      <h3>Scheduled garden care programs</h3>
      <p>Our Garden Care Program is tailored to keep your garden looking good all year</p>
      <svg class="go" viewBox="0 0 18 18"><circle cx="9" cy="9" r="9" fill="#4f8a1c"/><path d="M5 9h7M9 6l3 3-3 3" stroke="#fff" stroke-width="1.8" fill="none"/></svg>
    </article>
    <article class="card">
      <div class="thumb" role="img" aria-label="Maintained shrub garden"></div>
      <h3>Garden maintenance services</h3>
      <p>Our Garden Maintenance Services are once-off attendances when required</p>
      <svg class="go" viewBox="0 0 18 18"><circle cx="9" cy="9" r="9" fill="#4f8a1c"/><path d="M5 9h7M9 6l3 3-3 3" stroke="#fff" stroke-width="1.8" fill="none"/></svg>
    </article>
    <article class="card">
      <div class="thumb" role="img" aria-label="Green lawn beside a clipped hedge"></div>
      <h3>Reticulation services</h3>
      <p>Our Reticulation Service covers all aspects of garden and lawn irrigation</p>
      <svg class="go" viewBox="0 0 18 18"><circle cx="9" cy="9" r="9" fill="#4f8a1c"/><path d="M5 9h7M9 6l3 3-3 3" stroke="#fff" stroke-width="1.8" fill="none"/></svg>
    </article>
    <article class="card">
      <div class="thumb" role="img" aria-label="Large trees over a lawn"></div>
      <h3>Specialty garden services</h3>
      <p>Our Specialty Garden Services are designed to address specific issues in your garden</p>
      <svg class="go" viewBox="0 0 18 18"><circle cx="9" cy="9" r="9" fill="#4f8a1c"/><path d="M5 9h7M9 6l3 3-3 3" stroke="#fff" stroke-width="1.8" fill="none"/></svg>
    </article>
  </div>
</section>

<section class="section cta cta-one" role="img" aria-label="Seedlings sprouting in dark soil">
  <div class="inner">
    <h2>We can organise all that you need done in your garden.</h2>
    <p>Let us demonstrate our capabilities.</p>
    <span class="btn">Get in touch</span>
  </div>
</section>

<section class="section work">
  <h2>Recent Work</h2>
  <p class="lead">Over the years we have transformed many gardens Want to assess our capabilities?</p>
  <div class="gallery">
    <div class="tile g1" role="img" aria-label="Red and white flowers among foliage"></div>
    <div class="tile g2" role="img" aria-label="Garden area under trees"></div>
    <div class="tile g3" role="img" aria-label="Field of red poppies"></div>
    <div class="tile g4" role="img" aria-label="Close-up of young green seedlings"></div>
    <div class="tile g5" role="img" aria-label="Lawn and trees beside a house"></div>
    <div class="tile g6" role="img" aria-label="Freshly striped lawn with a mower"></div>
  </div>
  <span class="btn">View all</span>
</section>

<section class="section clients">
  <h2>Clients</h2>
  <svg class="arrow" style="left:52px" viewBox="0 0 22 40"><path d="M18 4L4 20l14 16" stroke="#777" stroke-width="3" fill="none"/></svg>
  <div class="logos">
    <div class="logo" style="color:#6aab2c">Norwave</div>
    <div class="logo">Kestrel Court</div>
    <div class="logo">Civic Care Office</div>
    <div class="logo">Ridgeline</div>
    <div class="logo">Homefront Response</div>
  </div>
  <svg class="arrow" style="left:1124px" viewBox="0 0 22 40"><path d="M4 4l14 16L4 36" stroke="#777" stroke-width="3" fill="none"/></svg>
</section>

<section class="section quote-sec">
  <div class="ring"><div class="photo" role="img" aria-label="Sprinklers watering a lawn at sunset"></div></div>
  <h2>What our clients<br>are saying</h2>
  <blockquote>“ Ewan is an absolute gem. I feel lucky to have him working on my garden. He is a very hard worker and gives 120%. Can recommend him to anyone. ”</blockquote>
  <cite>- Maree in Hillcrest</cite>
  <div class="pager">
    <span><svg width="8" height="10" viewBox="0 0 8 10"><path d="M6 1L2 5l4 4" stroke="#444" fill="none"/></svg></span>
    <span><svg width="8" height="10" viewBox="0 0 8 10"><path d="M2 1l4 4-4 4" stroke="#444" fill="none"/></svg></span>
  </div>
</section>

<section class="section cta cta-two" role="img" aria-label="Backlit grasses in a field at golden hour">
  <div class="inner">
    <h2>Working with trades people can be challengingWith Larkvale it isn’tYou’ll get to experience a professional working relationship with Larkvale.</h2>
    <span class="btn">Request a quote</span>
  </div>
</section>

<section class="section request">
  <h2>Request a quote</h2>
  <p class="lead">Collaboration begins with a conversation. Whether you’re interested in discussing a new project or simply wish to find out more about our services and what we can do for you, we are here to help. Send us a message below or<br><strong>call us at 0400 555 182</strong></p>
  <div class="form">
    <div class="field" style="left:0;top:0;width:217px">Full name</div>
    <div class="field" style="left:232px;top:0;width:217px">Email</div>
    <div class="field" style="left:0;top:48px;width:217px">Phone</div>
    <div class="field" style="left:232px;top:48px;width:217px">Subhurb</div>
    <div class="field msg" style="left:470px;top:0;width:442px">Message</div>
  </div>
  <span class="btn">Submit</span>
</section>

<footer class="section footer">
  <svg class="peak" viewBox="0 0 1200 90" preserveAspectRatio="none"><path d="M0 0H1200V70L600 0 0 70Z" fill="#fff"/><path d="M0 70L600 0 1200 70" stroke="#444" stroke-width="6" fill="none"/></svg>
  <div class="f-brand"><span class="brand-mark"></span><span class="brand-name">Larkvale</span></div>
  <p class="f-about">Scheduled Garden Care Programs and Garden Maintenance Services for residential, strata and commercial properties</p>
  <div class="f-col f-contact">
    <h4>Contact</h4>
    <p><svg width="12" height="12" viewBox="0 0 24 24"><path fill="#aaa" d="M6.6 10.8a15.1 15.1 0 0 0 6.6 6.6l2.2-2.2c.3-.3.7-.4 1-.2 1.1.4 2.3.6 3.6.6.6 0 1 .4 1 1V20c0 .6-.4 1-1 1A17 17 0 0 1 3 4c0-.6.4-1 1-1h3.5c.6 0 1 .4 1 1 0 1.3.2 2.5.6 3.6.1.3 0 .7-.2 1z"/></svg>0400 555 182</p>
    <p><svg width="12" height="10" viewBox="0 0 12 10"><rect width="12" height="10" fill="#aaa"/><path d="M0 0l6 5 6-5" stroke="#1e1e1e" fill="none"/></svg>ewan@larkvale.com.au</p>
    <div class="socials"><span>f</span><span>in</span><span>ig</span></div>
  </div>
  <div class="f-col f-nav">
    <h4>Navigation</h4>
    <ul><li>Home</li><li>About</li><li>Services</li><li>Work</li><li>Contact</li><li>Request a quote</li></ul>
  </div>
  <div class="f-rule"></div>
  <p class="f-copy">Copyright © 2020 Larkvale. All rights reserved.</p>
</footer>

</body>
</html>
```